Marrow Business Cards

Front of business card will have logo, name, address, & telephone number. Back of card will have a list of services provided - Roads, Substation Pads, Temporary Pads, Site Pads, Land Leveling, Powerline Row Cleaning, Land Clearing, Gates, Fencing, Construction Entrances, Excavation, Trenching, Underground Utilities, Directional Boring, Pile Driving. We are a construction company that uses heavy equipment like bulldozers, motor graders/blades, dump trucks, backhoes, hydro axes, & skid loaders. We build roads, pads, & install electric utility lines & waterlines underground. This logo is new. The word "Construction" can be smaller as uploaded 2 example edited logos. We will be using this card design for many employees.
Target Market(s)
Industrial Electric Powerline, Wind Turbine, Solar Panel, & Water Utility companies.
Contact Information for Business Card
Name/Position - Dorian Quale - Owner
Address: 4837 FM 582
Dunmore, TX 79418
Phone number - (325) 418-2906

```html
<!DOCTYPE html>
<html lang="en">
<head>
<meta charset="utf-8">
<title>Marrow Business Cards</title>
<link rel="stylesheet" href="https://fonts.googleapis.com/css2?family=Cinzel:wght@700&family=Poppins:wght@400;600&display=swap">
<style>
  :root {
    --maroon: #3b0d16;
    --paper: #f6f6f6;
    --back-paper: #ebebeb;
    --service-grey: #6d6d6d;
    --stage: #d9d4cf;
    --white: #ffffff;
  }
  * { box-sizing: border-box; margin: 0; padding: 0; }
  html, body {
    width: 1125px; height: 1200px; overflow: hidden;
    background: var(--stage);
    font-family: "Poppins", sans-serif;
  }
  .card {
    position: absolute; left: 150px; width: 826px; height: 470px;
    border-radius: 24px; overflow: hidden;
    box-shadow: 0 4px 10px rgba(0,0,0,0.25);
  }
  .card--front { top: 98px; background: var(--maroon); }
  .card--back { top: 632px; background: var(--back-paper); }

  .front__panel { position: absolute; inset: 0; width: 100%; height: 100%; }

  .wordmark {
    position: absolute; color: var(--maroon);
    font-family: "Poppins", sans-serif; font-weight: 600;
    text-transform: uppercase; line-height: 1;
  }
  .wordmark--front { left: 66px; top: 178px; }
  .wordmark--front .wordmark__name { display: block; font-size: 68px; letter-spacing: 1px; }
  .wordmark--front .wordmark__sub { display: block; font-size: 27px; margin-top: 16px; letter-spacing: 1px; }

  .holder {
    position: absolute; right: 54px; top: 52px; text-align: right; color: var(--white);
  }
  .holder__name { font-family: "Cinzel", serif; font-weight: 700; font-size: 30px; letter-spacing: 1px; line-height: 1.1; }
  .holder__role { font-size: 18px; margin-right: 4px; }

  .contact {
    position: absolute; right: 54px; top: 284px; text-align: right; color: var(--white);
    font-size: 18.5px; line-height: 23px;
  }
  .contact__address { margin-bottom: 12px; }
  .contact__line { display: flex; justify-content: flex-end; align-items: center; gap: 10px; }
  .contact__icon { width: 15px; height: 15px; fill: var(--white); flex: none; }

  .wordmark--back {
    left: 0; right: 0; top: 148px; text-align: center;
    font-size: 96px; letter-spacing: 3px;
  }
  .wordmark--back .wordmark__dot {
    display: inline-block; width: 26px; height: 26px; border-radius: 50%;
    background: var(--maroon); margin-left: 16px; vertical-align: middle;
  }
  .services {
    position: absolute; left: 0; right: 0; top: 362px; text-align: center;
    color: var(--service-grey); font-size: 18px; line-height: 22px;
  }
  .services__sep { font-size: 10px; vertical-align: middle; margin: 0 1px; }
</style>
</head>
<body>
  <section class="card card--front">
    <svg class="front__panel" viewBox="0 0 826 470" preserveAspectRatio="none" aria-hidden="true">
      <path d="M0 0 H300 C 520 120, 560 330, 220 470 H0 Z" fill="var(--paper)"/>
    </svg>
    <div class="wordmark wordmark--front">
      <span class="wordmark__name">Marrow</span>
      <span class="wordmark__sub">Construction</span>
    </div>
    <div class="holder">
      <div class="holder__name">DORIAN QUALE</div>
      <div class="holder__role">Owner</div>
    </div>
    <div class="contact">
      <div class="contact__address">4837 FM 582<br>Dunmore, TX 79418</div>
      <div class="contact__line">(325) 418-2906
        <svg class="contact__icon" viewBox="0 0 24 24" aria-hidden="true"><path d="M6.6 10.8a15 15 0 0 0 6.6 6.6l2.2-2.2a1 1 0 0 1 1-.25 11.4 11.4 0 0 0 3.6.57 1 1 0 0 1 1 1V20a1 1 0 0 1-1 1A17 17 0 0 1 3 4a1 1 0 0 1 1-1h3.5a1 1 0 0 1 1 1c0 1.25.2 2.45.57 3.57a1 1 0 0 1-.25 1z"/></svg>
      </div>
      <div class="contact__line">info@marrowconstruction.com
        <svg class="contact__icon" viewBox="0 0 24 24" aria-hidden="true"><path d="M2 5h20v14H2z M3 6l9 7 9-7" fill="var(--white)" stroke="var(--maroon)" stroke-width="1.5"/></svg>
      </div>
      <div class="contact__line">www.marrowconstruction.com
        <svg class="contact__icon" viewBox="0 0 24 24" aria-hidden="true"><circle cx="12" cy="12" r="10"/><path d="M2 12h20M12 2c3 3 3 17 0 20M12 2c-3 3-3 17 0 20" fill="none" stroke="var(--maroon)" stroke-width="1.5"/></svg>
      </div>
    </div>
  </section>

  <section class="card card--back">
    <div class="wordmark wordmark--back">Marrow<span class="wordmark__dot"></span></div>
    <p class="services">
      Roads <span class="services__sep">●</span> Substation Pads<span class="services__sep">●</span>Temporary Pads <span class="services__sep">●</span> Site Pads <span class="services__sep">●</span> Land Leveling<br>
      Powerline Row Cleaning <span class="services__sep">●</span> Land Clearing <span class="services__sep">●</span> Gates <span class="services__sep">●</span> Fencing <span class="services__sep">●</span> Construction Entrances<br>
      Excavation <span class="services__sep">●</span> Trenching <span class="services__sep">●</span> Underground Utilities <span class="services__sep">●</span> Directional Boring <span class="services__sep">●</span> Pile Driving
    </p>
  </section>
</body>
</html>
```